Brisk. Technology Logistics Software platform.

A modern looking and feeling website for a logistics software platform.
We connect retailers or wholesale parcel distributors to worldwide delivery solutions.
Methods tend to be road and air transport to final mile courier companies and post offices all over the world.
Our platform is for ecommerce distribution. A customer uses BRISK to enable them to connect to worldwide companies who will track and trace the delivery of their goods.

Target Market(s)

Onllne retailers. Markert Places such as Vorlix and Quendro. Wholesale third party logistics and packaging companies. Delivery companies based in the UK looking to expand overseas.

Number of Pages Required

5+ page

Font styles to use
Sans Serif

Colors
aaaaaa
dbdbdb
e6e6e6
c4c4c4
cbcbcb
c9c9c9
ec1f27
3176b5
0355a3

Requirements
Must have
• Landing Page.
• What we do.
• Who we are.
• Modules.
• Testimonies (password protected)
• Contact us.
• Interactive for mobile operating systems.
• Scrolling website.
• Short stock video showing on key pages.
• Very well polished fonts and buttons. A sharp and well executed website is required.
• Simplicity in feeling.
• To the point on message.
• Refined wording and copyrighting / messaging
• A link to our sub brand and product Brisk Parcels
• Capture interest so people read further.
Nice to have
• A polished video to explain what we do on landing page. Clipmarrow.net have some good options but not sure how professional they will look.
Should not have
• Bad graphics and colours.
• Not lots of clicks. Less as possible
• Complex message

```html
<!DOCTYPE html>
<html lang="en">
<head>
<meta charset="utf-8">
<title>Brisk. Technology – Logistics Software Platform</title>
<link href="https://fonts.googleapis.com/css2?family=Montserrat:wght@400;500;600;700;800&display=swap" rel="stylesheet">
<style>
:root{
  --red:#ec1f27;
  --blue:#3176b5;
  --navy:#0355a3;
  --grey-1:#aaaaaa;
  --grey-2:#dbdbdb;
  --grey-3:#e6e6e6;
  --grey-4:#c4c4c4;
  --ink:#1d1d1f;
  --text:#6a6a6a;
  --footer:#262223;
  --white:#ffffff;
}
*{box-sizing:border-box;margin:0;padding:0}
html,body{width:1200px;height:2320px;overflow:hidden}
body{font-family:'Montserrat',Arial,sans-serif;background:var(--white);color:var(--ink);position:relative}
a{color:inherit;text-decoration:none}
.abs{position:absolute}

/* header */
.site-header{position:absolute;left:0;top:0;width:1200px;height:80px;background:var(--white)}
.brand{position:absolute;left:80px;top:22px;display:flex;align-items:center;gap:8px;color:var(--red);font-weight:700;font-size:26px;letter-spacing:-.5px}
.brand-dot{width:14px;height:14px;border-radius:50%;background:var(--red)}
.main-nav{position:absolute;top:34px;left:368px;display:flex;gap:0;font-size:11px;font-weight:600;letter-spacing:.6px;color:var(--ink)}
.main-nav a{position:absolute;white-space:nowrap}
.main-nav .active{color:var(--blue)}
.main-nav .active::after{content:"";position:absolute;left:-6px;right:-6px;top:44px;height:2px;background:var(--blue)}
.btn-demo{position:absolute;left:993px;top:23px;width:126px;height:32px;background:var(--blue);color:var(--white);font-size:10.5px;font-weight:600;letter-spacing:.6px;display:flex;align-items:center;justify-content:center;box-shadow:0 1px 3px rgba(0,0,0,.25)}

/* hero */
.hero{position:absolute;left:0;top:80px;width:1200px;height:520px;background:linear-gradient(100deg,#2f3133 0%,#4a4d50 40%,#6c6f71 65%,#3d3f41 100%)}
.hero-title{position:absolute;left:156px;top:170px;color:var(--white);font-size:29px;font-weight:800;line-height:39px;letter-spacing:.3px}
.btn{display:flex;align-items:center;justify-content:center;font-size:10px;font-weight:700;letter-spacing:.8px;position:absolute}
.btn-red{background:var(--red);color:var(--white)}
.btn-blue{background:var(--blue);color:var(--white)}
.hero .btn{left:156px;top:310px;width:142px;height:31px}
.play{position:absolute;left:872px;top:189px;width:142px;height:142px;border-radius:50%;background:rgba(255,255,255,.28);display:flex;align-items:center;justify-content:center}

/* intro */
.intro-title{position:absolute;left:156px;top:658px;font-size:24px;font-weight:500;line-height:29px;color:var(--ink)}
.intro-text{position:absolute;left:156px;width:650px;font-size:12px;line-height:17.5px;color:var(--text)}
.intro .btn{top:896px;height:32px}
.brand-panel{position:absolute;left:840px;top:600px;width:204px;height:390px;background:var(--grey-3)}
.panel-mark{position:absolute;left:0;width:204px;text-align:center;font-weight:700;font-size:22px;color:var(--red)}
.panel-rule{position:absolute;left:30px;top:196px;width:144px;height:1px;background:var(--grey-4)}

/* what we do */
.services{position:absolute;left:0;top:990px;width:1200px;height:448px;background:linear-gradient(180deg,#3a2a22 0%,#5b4232 50%,#3e2f28 100%);color:var(--white);text-align:center}
.eyebrow{position:absolute;left:0;width:1200px;top:82px;font-size:11px;font-weight:600;letter-spacing:1.2px}
.services-title{position:absolute;left:0;width:1200px;top:104px;font-size:24px;font-weight:600;line-height:29px}
.tab{position:absolute;top:192px;width:423px;font-size:14px;font-weight:700;letter-spacing:1px}
.tab-line{position:absolute;top:226px;height:2px}
.services-text{position:absolute;left:196px;width:808px;top:258px;font-size:12px;line-height:18px}
.services .btn{left:529px;top:336px;width:127px;height:32px}

/* features */
.feature-title{position:absolute;left:156px;top:1500px;width:420px;font-size:20px;font-weight:600;line-height:23px}
.feature-list{position:absolute;left:156px;top:1598px;list-style:none;font-size:12px;color:var(--text)}
.feature-list li{height:24px;display:flex;align-items:center;gap:10px}
.btn-outline{position:absolute;left:156px;top:1787px;width:144px;height:32px;border:1.5px solid var(--red);color:var(--red)}
.feature-photo{position:absolute;left:612px;top:1503px;width:432px;height:318px;background:linear-gradient(135deg,#d9d2c9 0%,#c4b3a2 45%,#9c8572 100%)}

/* footer */
.site-footer{position:absolute;left:0;top:1982px;width:1200px;height:338px;background:var(--footer)}
.cta-box{position:absolute;left:156px;top:1905px;width:888px;height:157px;background:var(--grey-3);box-shadow:0 2px 6px rgba(0,0,0,.2)}
.cta{position:absolute;top:0;width:296px;height:157px;text-align:center}
.cta svg{position:absolute;left:124px;top:32px}
.cta-label{position:absolute;left:0;width:296px;top:101px;font-size:14px;font-weight:600;color:var(--navy)}
.cta-label.accent{color:var(--red);text-decoration:underline}
.cta-divider{position:absolute;top:30px;width:1px;height:97px;background:var(--grey-4)}
.foot-head{position:absolute;top:2127px;font-size:11px;font-weight:600;letter-spacing:1.2px;color:var(--blue)}
.foot-text{position:absolute;font-size:11.5px;line-height:23px;color:#d9d9d9}
.foot-text u{text-decoration:underline}
.social{position:absolute;top:2165px;width:33px;height:33px;border-radius:50%;background:#8a8a8a}
.social.active{background:var(--red)}
.foot-rule{position:absolute;left:132px;top:2245px;width:936px;height:1px;background:#3d393a}
.copyright{position:absolute;left:0;width:1200px;top:2274px;text-align:center;font-size:11px;color:#cfcfcf}
.copyright .hl{color:var(--red)}
</style>
</head>
<body>

<header class="site-header">
  <a class="brand" href="#"><span class="brand-dot"></span>Brisk. Technology</a>
  <nav class="main-nav">
    <a class="active" style="left:0">HOME</a>
    <a style="left:71px">WHAT WE DO</a>
    <a style="left:184px">WHO WE ARE</a>
    <a style="left:298px">MODULES</a>
    <a style="left:390px">TESTIMAONIES</a>
    <a style="left:510px">CONTACT US</a>
  </nav>
  <a class="btn-demo" href="#">REQUEST A DEMO</a>
</header>

<section class="hero" role="img" aria-label="Warehouse interior with tall racking of stacked parcels">
  <h1 class="hero-title">MANAGE YOUR CARRIERS,<br>YOUR DELIVERY SPEEDS, AND<br>YOUR COSTS</h1>
  <a class="btn btn-red" href="#">DISCOVER PRODUCTS</a>
  <div class="play">
    <svg width="44" height="48" viewBox="0 0 44 48"><path d="M6 4 L40 24 L6 44 Z" fill="#fff"/></svg>
  </div>
</section>

<section class="intro">
  <h2 class="intro-title">Brisk. Technology &amp; Parcel Solutions<br>Built To Help Develop &amp; Manage Your Global<br>Delivery Network</h2>
  <p class="intro-text" style="top:760px">Working closely with Ecommerce, Brisk. Technology have developed solutions purely focused on delivering what's required within the global delivery marketplace. Meeting all needs and more for Retailers and Global Delivery Solution providers</p>
  <p class="intro-text" style="top:832px">Allowing customers to grow at a fast pace; most importantly providing tools to help them manage their global delivery network supported by "Dynamic Real Time Visibility" management tools.</p>
  <a class="btn btn-blue" href="#" style="left:156px;width:143px">BRISK PARCEL</a>
  <a class="btn btn-red" href="#" style="left:315px;width:144px">BRISK TECHNOLOGY</a>
  <aside class="brand-panel">
    <div class="panel-mark" style="top:86px">Brisk Parcels</div>
    <div class="panel-rule"></div>
    <div class="panel-mark" style="top:280px">Brisk. Technology</div>
  </aside>
</section>

<section class="services" role="img" aria-label="Aerial view of a container port with stacked shipping containers">
  <p class="eyebrow">WHAT WE DO</p>
  <h2 class="services-title">Solution Developed To Help you Build &amp; Manage Your<br>Global Delivery&nbsp; Network</h2>
  <div class="tab" style="left:160px">LOGISTIC PROVIDERS</div>
  <div class="tab" style="left:617px">RETAILERS DELIVERY</div>
  <div class="tab-line" style="left:198px;width:410px;background:var(--red)"></div>
  <div class="tab-line" style="left:612px;width:432px;background:rgba(255,255,255,.35)"></div>
  <svg class="abs" style="left:360px;top:226px" width="24" height="12" viewBox="0 0 24 12"><path d="M2 1 L12 10 L22 1" fill="none" stroke="#ec1f27" stroke-width="2"/></svg>
  <p class="services-text">Brisk Technology gives logistic companies to enhance their platform to implement and manage their extended delivery partners.&nbsp; Full end to end solution covers all the key elements, allowing Carriers to implement services manage all delivery activities via 1 single platform ...</p>
  <a class="btn btn-red" href="#">READ MORE</a>
</section>

<section class="features">
  <h2 class="feature-title">Brisk Parcels Delivering To Complex Lanes Providing A Fully Managed Secure Delivery Experience</h2>
  <ul class="feature-list">
    <li><svg width="12" height="10" viewBox="0 0 12 10"><path d="M1 5 L4.5 8.5 L11 1" fill="none" stroke="#3176b5" stroke-width="2"/></svg>Fully Managed End To End Delivery Solution</li>
    <li><svg width="12" height="10" viewBox="0 0 12 10"><path d="M1 5 L4.5 8.5 L11 1" fill="none" stroke="#3176b5" stroke-width="2"/></svg>Delivery Solution Suited For Local Consumers</li>
    <li><svg width="12" height="10" viewBox="0 0 12 10"><path d="M1 5 L4.5 8.5 L11 1" fill="none" stroke="#3176b5" stroke-width="2"/></svg>Last Mile Printed At Pack Bench</li>
    <li><svg width="12" height="10" viewBox="0 0 12 10"><path d="M1 5 L4.5 8.5 L11 1" fill="none" stroke="#3176b5" stroke-width="2"/></svg>Supported By End To End Tracking</li>
    <li><svg width="12" height="10" viewBox="0 0 12 10"><path d="M1 5 L4.5 8.5 L11 1" fill="none" stroke="#3176b5" stroke-width="2"/></svg>Secure Customs Set Up</li>
    <li><svg width="12" height="10" viewBox="0 0 12 10"><path d="M1 5 L4.5 8.5 L11 1" fill="none" stroke="#3176b5" stroke-width="2"/></svg>Service Supported By Account Management Tools</li>
    <li><svg width="12" height="10" viewBox="0 0 12 10"><path d="M1 5 L4.5 8.5 L11 1" fill="none" stroke="#3176b5" stroke-width="2"/></svg>Service Managed Bt Brisk Parcels Service Support Team</li>
  </ul>
  <a class="btn btn-outline" href="#">LET'S TALK</a>
  <div class="feature-photo" role="img" aria-label="Retailer in a clothing boutique checking orders on a tablet"></div>
</section>

<footer class="site-footer"></footer>

<div class="cta-box">
  <div class="cta" style="left:0">
    <svg width="48" height="48" viewBox="0 0 48 48"><path d="M10 6 L18 6 L21 15 L16 19 C19 26 23 30 29 33 L33 28 L42 31 L42 39 C42 41 40 43 38 43 C21 42 7 28 6 10 C6 8 8 6 10 6 Z" fill="none" stroke="#1d1d1f" stroke-width="2.2" stroke-linejoin="round"/><rect x="28" y="4" width="14" height="12" rx="2" fill="none" stroke="#ec1f27" stroke-width="2"/></svg>
    <div class="cta-label">Need Help? Contact Us</div>
  </div>
  <div class="cta-divider" style="left:296px"></div>
  <div class="cta" style="left:296px">
    <svg width="48" height="48" viewBox="0 0 48 48"><circle cx="20" cy="10" r="6" fill="none" stroke="#ec1f27" stroke-width="2"/><path d="M17 12 L17 30 L13 27 C11 25 8 27 10 30 L18 43 L36 43 L38 30 C38 26 36 24 33 24 L23 22 L23 12 C23 9 17 9 17 12 Z" fill="none" stroke="#1d1d1f" stroke-width="2.2" stroke-linejoin="round"/></svg>
    <div class="cta-label accent">Request a Demo</div>
  </div>
  <div class="cta-divider" style="left:592px"></div>
  <div class="cta" style="left:592px">
    <svg width="48" height="48" viewBox="0 0 48 48"><path d="M10 24 C10 14 16 8 24 8 C32 8 38 14 38 24" fill="none" stroke="#1d1d1f" stroke-width="2.2"/><rect x="7" y="22" width="6" height="11" rx="2" fill="none" stroke="#1d1d1f" stroke-width="2"/><rect x="35" y="22" width="6" height="11" rx="2" fill="none" stroke="#1d1d1f" stroke-width="2"/><rect x="8" y="36" width="32" height="8" rx="2" fill="none" stroke="#1d1d1f" stroke-width="2"/><circle cx="24" cy="40" r="1.5" fill="#ec1f27"/></svg>
    <div class="cta-label">Request a Quote</div>
  </div>
</div>

<div class="foot-head" style="left:156px">ADDRESS:</div>
<p class="foot-text" style="left:156px;top:2158px">12780 Larkmoor Avenue,<br>Fenwick, RL USA - 40215</p>
<div class="foot-head" style="left:460px">CONTACT US:</div>
<p class="foot-text" style="left:460px;top:2158px">Phone: 555 - 014 - 2288<br>Email:&nbsp; <u>info@brisktechnology.com</u></p>
<div class="foot-head" style="left:764px">FOLLOW US:</div>
<a class="social" href="#" aria-label="Social profile one" style="left:765px"></a>
<a class="social active" href="#" aria-label="Social profile two" style="left:806px"></a>
<a class="social" href="#" aria-label="Social profile three" style="left:848px"></a>
<a class="social" href="#" aria-label="Social profile four" style="left:890px"></a>
<svg class="abs" style="left:1110px;top:2128px" width="18" height="22" viewBox="0 0 18 22" aria-label="Back to top"><path d="M9 1 L17 21 L9 16 L1 21 Z" fill="#3176b5"/></svg>
<div class="foot-rule"></div>
<p class="copyright">© 2018 <span class="hl">Brisk Technology</span>. All Rights Reserved.&nbsp;&nbsp;&nbsp; Terms &amp; Conditions&nbsp;&nbsp; |&nbsp;&nbsp; Privacy Policy</p>

</body>
</html>
```